Business Card & Logo Design - Hedge Fund

We need a business card and logo design for a hedge fund. The hedge fund is named Morvane Equity LLC. Morvane Equity was created by finance professors and the strategy is based academic research that looks for patterns in stock prices. The design should look conservative, solid, strong. We favor a classic style - nothing flashy. The logo can relate to the name Morvane Equity, or it could involve a symbol design that connotes "science" . We are open to ideas. We do not want alot of colors - but if any, color - blue is preferred. The font that seems to look best for the name (Morvane Equity) is arial black. We are open to ideas. Most important - we want to see a mock up of an actual business card with the logo concept embedded. The business card should include space for : company name, individual name, position title, cell phone, address. We hope to have this work done by Sept. 8.

Target Market(s)

We will be meeting with and giving the business card to institutions and high net worth individuals.

Industry/Entity Type

Investment Advisory

Contact Information for Business Card

Company name - Morvane Equity LLC
Individual name - Peter Dalby
Title - Portfolio Manager
Cell - (412) 555-0187
Address - 2650 Birchmont Lane, Suite 300, Atlanta GA 30327

Font styles to use
Other font styles liked:
• Arial

Colors
3277b5
0255a3
85acd3
cedeed
fdf9cf
d9d9d9
e6e6e6
f04a50
6b449b

Requirements
Must have
• Must have card details that are sited above.
• We would like a logo related to the name (Morvane Equity) or concept of the fund.
Nice to have
• We want conservative / understated / clean crisp look.
• If any colors - we prefer conservative appearance - blue / gray.
• I have enclosed an example of a card style that looks attractive - please do not exactly copy this card. This is not our company or logo. I feel the layout is attractive - just as an example
Should not have
• Avoid too much color.
• I have selected some preferred colors. Please do not use all of the colors - I have selected a few that might work - but I am not sure. We are open to your ideas so please do not feel the need to use all or any of these.

```html
<!DOCTYPE html>
<html lang="en">
<head>
<meta charset="utf-8">
<title>Morvane Equity LLC — Business Card</title>
<link rel="stylesheet" href="https://fonts.googleapis.com/css2?family=Montserrat:wght@700&family=Open+Sans:wght@400;600&display=swap">
<style>
  :root {
    --stage: #262628;
    --brand-blue: #3a309f;
    --brand-blue-deep: #2c2487;
    --ink-navy: #2a2580;
    --ink-grey: #8a8a90;
    --paper: #ffffff;
    --soft-grey: #e6e6e6;
  }
  * { box-sizing: border-box; margin: 0; padding: 0; }
  html, body { width: 1200px; height: 660px; overflow: hidden; }
  body {
    background: var(--stage);
    font-family: "Open Sans", Arial, sans-serif;
    position: relative;
  }
  .card {
    position: absolute;
    top: 187px;
    width: 500px;
    height: 286px;
    border-radius: 3px;
    overflow: hidden;
    box-shadow: 0 14px 30px rgba(0,0,0,.45);
  }
  /* Front */
  .card-front { left: 70px; }
  .front-texture {
    position: absolute; inset: 0;
    background: linear-gradient(135deg, var(--brand-blue) 0%, var(--brand-blue-deep) 100%);
  }
  .front-wordmark {
    position: absolute; left: 0; right: 0; top: 112px;
    text-align: center;
    font-family: "Montserrat", Arial, sans-serif;
    font-weight: 700;
    font-size: 34px;
    line-height: 1.15;
    letter-spacing: 2px;
    color: var(--paper);
    text-transform: uppercase;
  }
  /* Back */
  .card-back { left: 630px; background: var(--paper); }
  .back-band {
    position: absolute; left: 0; right: 0; bottom: 0; height: 12px;
    background: var(--brand-blue);
  }
  .back-logo {
    position: absolute; left: 30px; top: 62px;
    display: flex; align-items: center; gap: 10px;
  }
  .logo-square {
    width: 30px; height: 30px;
    background: var(--ink-navy);
  }
  .logo-name {
    font-family: "Montserrat", Arial, sans-serif;
    font-weight: 700;
    font-size: 22px;
    line-height: 1.05;
    color: var(--ink-navy);
    text-transform: uppercase;
    letter-spacing: .5px;
  }
  .person {
    position: absolute; right: 26px; top: 56px; text-align: left;
  }
  .person-name {
    font-size: 22px; color: var(--ink-grey); font-weight: 400;
  }
  .person-title {
    font-size: 13px; color: var(--ink-navy); font-weight: 600;
    display: flex; align-items: center; gap: 6px;
  }
  .person-title::after {
    content: ""; width: 18px; height: 2px; background: var(--ink-navy);
  }
  .rule { position: absolute; height: 2px; background: var(--ink-navy); }
  .rule-top { left: 30px; width: 290px; top: 124px; }
  .rule-contact { left: 20px; width: 300px; top: 176px; }
  .contact {
    position: absolute; left: 24px; top: 190px;
    font-size: 13px; color: var(--ink-navy); line-height: 1.5;
  }
  .contact-row { display: flex; gap: 8px; align-items: flex-start; }
  .contact-row svg { flex: none; margin-top: 3px; }
</style>
</head>
<body>
  <section class="card card-front" aria-label="Card front">
    <div class="front-texture" role="img" aria-label="Deep blue textured card face with a faint repeating pattern"></div>
    <div class="front-wordmark">Morvane<br>Equity LLC</div>
  </section>

  <section class="card card-back" aria-label="Card back">
    <div class="back-logo">
      <span class="logo-square"></span>
      <span class="logo-name">Morvane<br>Equity LLC</span>
    </div>
    <div class="person">
      <p class="person-name">Peter Dalby</p>
      <p class="person-title">Portfolio Manager</p>
    </div>
    <span class="rule rule-top"></span>
    <span class="rule rule-contact"></span>
    <div class="contact">
      <div class="contact-row">
        <svg width="12" height="12" viewBox="0 0 24 24" aria-hidden="true"><path fill="#2a2580" d="M6.6 10.8a15 15 0 0 0 6.6 6.6l2.2-2.2a1 1 0 0 1 1-.25 11.4 11.4 0 0 0 3.6.57 1 1 0 0 1 1 1V20a1 1 0 0 1-1 1A17 17 0 0 1 3 4a1 1 0 0 1 1-1h3.5a1 1 0 0 1 1 1c0 1.25.2 2.45.57 3.6a1 1 0 0 1-.25 1z"/></svg>
        <span>(412) 555-0187</span>
      </div>
      <div class="contact-row">
        <svg width="12" height="12" viewBox="0 0 24 24" aria-hidden="true"><path fill="#2a2580" d="M12 2a7 7 0 0 0-7 7c0 5.25 7 13 7 13s7-7.75 7-13a7 7 0 0 0-7-7zm0 9.5A2.5 2.5 0 1 1 12 6.5a2.5 2.5 0 0 1 0 5z"/></svg>
        <span>2650 Birchmont Lane<br>Suite 300, Atlanta GA 30327</span>
      </div>
    </div>
    <div class="back-band"></div>
  </section>
</body>
</html>
```